Corvello Paintless Dent Removal

Our company works on vehicles removing dents using a highly skilled trade which the metal is massaged out with special tools without disturbing the original paint, hence paintless dent removal. Besides keeping the paint and metal original its also very environmentally friendly since no paint or toxic fillers are used. Also we we are one of the most experienced companies in the business with 25 years

Target Market(s)

Retail Automobile consumers, Auto Dealerships and Auto Body Shops

Industry/Entity Type

Auto Repair

Contact Information for Business Card

Dwight Halvorsen
PO Box 538 Ashbrook, NY 11892
631-472-8169
corvellopdr@mailnest.example
website corvellopdr.example
youtube corvello paintless dent removal
25 years of experience removing Dents, Dings and Hail Damage

Font styles to use
Serif
Sans Serif

Colors

Designer to choose colors to be used in the design.

Requirements
Must have
• I do like things that are simple but classy and somewhat bold, also I like my logo so that should be somewhat important

```html
<!DOCTYPE html>
<html lang="en">
<head>
<meta charset="utf-8">
<title>Corvello Paintless Dent Removal – Business Card</title>
<link rel="stylesheet" href="https://fonts.googleapis.com/css2?family=Arimo:wght@400;700&display=swap">
<style>
  :root {
    --backdrop: #1b1b1b;
    --card-white: #ffffff;
    --navy: #13284e;
    --green: #7ac31d;
    --ink: #1f1f1f;
    --rule: #9aa3ad;
    --grad-navy: #0c2749;
    --grad-green: #7cc412;
  }
  * { margin: 0; padding: 0; box-sizing: border-box; }
  html, body {
    width: 1200px; height: 900px; overflow: hidden;
    background: var(--backdrop);
    font-family: "Arimo", Arial, sans-serif;
  }
  .stage { position: relative; width: 1200px; height: 900px; }
  .card {
    position: absolute; top: 170px; width: 347px; height: 561px;
    box-shadow: 0 2px 6px rgba(0,0,0,.6);
    text-align: center;
  }
  .card--front { left: 259px; background: var(--card-white); color: var(--ink); }
  .card--back {
    left: 631px; color: #fff;
    background: linear-gradient(135deg, var(--grad-navy) 0%, #3d7a2c 22%, var(--grad-green) 48%, #6fb516 62%, #2f6a3a 82%, var(--grad-navy) 100%);
  }
  .wordmark {
    position: absolute; left: 0; right: 0;
    font-weight: 700; line-height: 1.1;
  }
  .card--front .wordmark { top: 118px; font-size: 26px; color: var(--navy); }
  .card--back .wordmark { top: 248px; font-size: 26px; color: #fff; }
  .wordmark .sub { display: block; font-size: 26px; }
  .holder {
    position: absolute; top: 250px; left: 0; right: 0;
    font-size: 21px; font-weight: 700; letter-spacing: .3px;
  }
  .holder .first { color: var(--navy); }
  .holder .last { color: var(--green); }
  .divider { position: absolute; left: 88px; width: 170px; height: 24px; }
  .contact {
    position: absolute; left: 0; right: 0;
    font-size: 16px; line-height: 21px;
  }
  .tagline {
    position: absolute; top: 452px; left: 0; right: 0;
    font-size: 19px; line-height: 25px; text-transform: uppercase; letter-spacing: .2px;
  }
</style>
</head>
<body>
<main class="stage">

  <section class="card card--front">
    <div class="wordmark">CORVELLO<span class="sub">Paintless Dent Removal</span></div>

    <div class="holder"><span class="first">DWIGHT</span> <span class="last">HALVORSEN</span></div>

    <svg class="divider" style="top:296px" viewBox="0 0 170 24" aria-hidden="true">
      <line x1="0" y1="12" x2="40" y2="12" stroke="#4a6a9a" stroke-width="1"/>
      <line x1="130" y1="12" x2="170" y2="12" stroke="#4a6a9a" stroke-width="1"/>
      <circle cx="57" cy="12" r="11" fill="var(--navy)"/>
      <path d="M51 15 q6 -7 12 0 v2 h-12z M53 10 h8" fill="#fff" stroke="#fff" stroke-width="1.4"/>
      <circle cx="85" cy="12" r="11" fill="var(--navy)"/>
      <rect x="79" y="8" width="12" height="8" fill="none" stroke="#fff" stroke-width="1.3"/>
      <path d="M79 8 l6 5 l6 -5" fill="none" stroke="#fff" stroke-width="1.3"/>
      <circle cx="113" cy="12" r="11" fill="var(--navy)"/>
      <circle cx="113" cy="12" r="6" fill="none" stroke="#fff" stroke-width="1.3"/>
      <path d="M107 12 h12 M113 6 q-4 6 0 12 M113 6 q4 6 0 12" fill="none" stroke="#fff" stroke-width="1"/>
    </svg>

    <div class="contact" style="top:325px">631-472-8169<br>corvellopdr@mailnest.example<br>corvellopdr.example</div>

    <svg class="divider" style="top:403px" viewBox="0 0 170 24" aria-hidden="true">
      <line x1="0" y1="12" x2="70" y2="12" stroke="var(--rule)" stroke-width="1"/>
      <line x1="100" y1="12" x2="170" y2="12" stroke="var(--rule)" stroke-width="1"/>
      <circle cx="85" cy="12" r="12" fill="var(--navy)"/>
    </svg>

    <div class="contact" style="top:431px">corvello paintless dent removal</div>

    <svg class="divider" style="top:466px" viewBox="0 0 170 24" aria-hidden="true">
      <line x1="0" y1="12" x2="70" y2="12" stroke="var(--rule)" stroke-width="1"/>
      <line x1="100" y1="12" x2="170" y2="12" stroke="var(--rule)" stroke-width="1"/>
      <circle cx="85" cy="12" r="12" fill="var(--navy)"/>
      <path d="M85 20 C80 14 79 11 79 9 a6 6 0 0 1 12 0 c0 2 -1 5 -6 11z" fill="#fff"/>
      <circle cx="85" cy="9" r="2.2" fill="var(--navy)"/>
    </svg>

    <div class="contact" style="top:497px">PO Box 538 Ashbrook NY 11892</div>
  </section>

  <section class="card card--back">
    <div class="wordmark">CORVELLO<span class="sub">Paintless Dent Removal</span></div>
    <p class="tagline">25 years of experience<br>removing dents, dings<br>and hail damage</p>
  </section>

</main>
</body>
</html>
```